BrightHollowMoney(.net) needs website & logo design

We need our website mock-up made into a reality! We are wanting to launch a multifaceted website for all things financial - i.e. blogs, financial wellness information, and a network of redirect links.
We have an existing mock-up, which I will include, but are open to your creative approach!

Industry/Entity Type

Finance

Coding

Coded - Design and coding required

Number of Pages Required

1 page

Requirements
Must have
• Corresponding logo

```html
<!DOCTYPE html>
<html lang="en">
<head>
<meta charset="utf-8">
<title>BrightHollowMoney – A Clear Path to Financial Wellness</title>
<link href="https://fonts.googleapis.com/css2?family=Poppins:wght@300;400;500;600;700&display=swap" rel="stylesheet">
<style>
:root{
  --teal:#7dcfbf;
  --teal-soft:#d7efe9;
  --forest:#0b5d4b;
  --forest-dark:#08463a;
  --ink:#1b1b1b;
  --grey-card:#d6d6d6;
  --muted:#555;
  --white:#fff;
  --red:#a63b2e;
}
*{box-sizing:border-box;margin:0;padding:0}
html,body{width:1200px;height:4515px;overflow:hidden}
body{font-family:'Poppins',sans-serif;color:var(--ink);background:var(--white);position:relative}
section,header,footer{position:absolute;left:0;width:1200px}
.btn{position:absolute;display:flex;align-items:center;justify-content:center;font-size:11px;letter-spacing:.5px;border-radius:6px;text-transform:uppercase}
.btn-outline-light{border:1.5px solid var(--white);color:var(--white)}
.btn-outline-teal{border:1.5px solid var(--teal);color:var(--teal)}
.btn-outline-dark{border:1.5px solid var(--ink);color:var(--ink)}
.eyebrow{position:absolute;font-size:17px;font-weight:500;letter-spacing:2px;text-transform:uppercase}
.arrow-list{position:absolute;list-style:none}
.arrow-list li{display:flex;align-items:center;gap:18px;font-size:12.5px;height:59px}
.arrow-list li::before{content:"";width:22px;height:1.5px;background:currentColor;display:block}
.photo{position:absolute}

/* header */
.site-header{top:0;height:93px;background:var(--white)}
.brand{position:absolute;left:120px;top:27px;display:flex;align-items:center;gap:8px;font-size:15px;line-height:17px;font-weight:600;color:var(--forest)}
.brand i{width:20px;height:20px;border-radius:50%;background:var(--teal);display:block;flex:none}
.main-nav{position:absolute;left:279px;top:36px;display:flex;gap:34px;font-size:12px;font-weight:500}
.main-nav a{color:var(--ink);text-decoration:none}
.main-nav a.active{color:var(--teal)}
.search{position:absolute;left:866px;top:33px;width:124px;height:25px;background:#eee;border-radius:4px;font-size:8px;color:#999;padding:7px 8px}
.search svg{position:absolute;right:7px;top:6px}
.account{position:absolute;left:999px;top:30px;border-left:2px solid var(--ink);padding-left:10px;font-size:10px;font-weight:600;height:30px;line-height:30px}

/* hero */
.hero{top:93px;height:571px}
.hero .photo{inset:0;background:linear-gradient(100deg,#8a8f93 0%,#a9abac 30%,#5d6268 55%,#2f3a48 75%,#51575e 100%)}
.hero h1{position:absolute;left:122px;top:105px;font-size:48px;line-height:54px;font-weight:700;color:var(--white);letter-spacing:.5px}
.hero p{position:absolute;left:122px;top:280px;width:370px;font-size:13px;line-height:16px;color:var(--white)}
.hero .signup{position:absolute;left:122px;top:340px;font-size:17px;font-weight:600;letter-spacing:3px;color:var(--white)}
.hero .email{position:absolute;left:122px;top:382px;width:234px;height:37px;background:var(--white);border-radius:4px;font-size:9px;color:#888;padding:13px 11px}
.hero .go{left:121px;top:429px;width:116px;height:32px;background:var(--teal);color:var(--white);border-radius:4px}

/* about */
.about{top:664px;height:867px;background:var(--teal)}
.feature-card{position:absolute;left:122px;top:54px;width:956px;height:433px;background:var(--forest)}
.feature-card .photo{left:0;top:0;width:477px;height:433px;background:linear-gradient(90deg,#e8ecee,#c9ced2 60%,#dde1e3)}
.feature-card h2{position:absolute;left:566px;top:72px;width:300px;font-size:27px;line-height:31px;font-weight:400;color:var(--white)}
.feature-card .card-btn{left:568px;top:261px;width:114px;height:30px}
.about .eyebrow{left:122px;top:532px;color:var(--forest)}
.about .lead{position:absolute;left:122px;top:575px;width:450px;font-size:25px;line-height:31px;color:var(--white)}
.about .lead-btn{left:122px;top:741px;width:114px;height:30px}
.about .arrow-list{left:710px;top:538px;color:var(--white)}

/* news */
.news{top:1531px;height:594px}
.news .eyebrow{left:122px;top:44px;color:var(--forest)}
.news-card{position:absolute;top:102px;width:314px;height:382px;background:var(--grey-card);padding:66px 20px 0}
.news-card .tag{font-size:9px;color:var(--red);letter-spacing:.5px}
.news-card h3{font-size:20px;line-height:29.5px;font-weight:400;letter-spacing:1px;margin-top:10px}
.news-card .date{font-size:8.5px;color:var(--muted);margin-top:8px}
.divider{position:absolute;top:102px;width:2px;height:388px;background:#444}
.pager{position:absolute;display:flex;gap:8px}
.pager span{width:36px;height:35px;border:1.5px solid var(--teal);border-radius:6px;display:flex;align-items:center;justify-content:center}
.pager span.dim{opacity:.45}

/* impact */
.impact{top:2125px;height:740px;background:var(--teal-soft)}
.impact .eyebrow{left:122px;top:49px;color:var(--forest)}
.impact .lead{position:absolute;left:122px;top:98px;font-size:26px;line-height:31px;font-weight:500}
.impact .arrow-list{left:685px;top:80px;color:var(--ink)}
.impact .slide-photo{left:122px;top:272px;width:397px;height:352px;background:linear-gradient(180deg,#d7d5cf 0%,#c9a98a 40%,#5d7a4a 70%,#6f9a3a 100%)}
.esg{position:absolute;left:519px;top:272px;width:396px;height:352px;background:var(--teal);color:var(--white);padding:0 28px}
.esg h3{margin-top:110px;font-size:22px;font-weight:400;white-space:nowrap}
.esg p{margin-top:12px;font-size:11px;line-height:16px;width:290px}
.esg .btn{left:29px;top:233px;width:116px;height:30px}
.impact .next-photo{left:944px;top:272px;width:256px;height:352px;background:linear-gradient(135deg,#c58c5a,#8a6a4e 50%,#d7c8b4)}

/* trending */
.trending{top:2865px;height:525px}
.trending h2{position:absolute;left:121px;top:85px;width:380px;font-size:25px;line-height:31px;font-weight:600}
.trending p{position:absolute;left:121px;width:330px;font-size:12px;line-height:16.5px}
.trending .btn{left:121px;top:397px;width:114px;height:36px}
.trending .photo{left:526px;top:64px;width:548px;height:398px;background:linear-gradient(120deg,#2e2520,#5a4434 45%,#a88e74 75%,#d9d4cb)}

/* tools */
.tools{top:3390px;height:345px;background:linear-gradient(180deg,#454545 0%,#393939 60%,#151515 100%)}
.tool{position:absolute;top:81px;width:138px}
.tool .box{height:138px;border:2px solid #ddd;display:flex;align-items:center;justify-content:center}
.tool .label{text-align:center;color:var(--white);font-size:14px;font-weight:600;line-height:18px;margin-top:30px}

/* questions */
.questions{top:3735px;height:204px}
.questions h2{position:absolute;left:121px;top:48px;font-size:34px;font-weight:600}
.questions p{position:absolute;left:123px;top:110px;width:640px;font-size:11.5px;line-height:15px}
.questions .btn{left:830px;top:91px;width:114px;height:34px;background:var(--teal);color:var(--white);border-radius:6px}

/* newsletter & footer */
.site-footer{top:3939px;height:576px;background:var(--teal);color:var(--white)}
.newsletter{position:absolute;left:122px;top:61px;width:956px;height:177px;background:var(--forest)}
.newsletter h2{position:absolute;left:18px;top:52px;font-size:26px;line-height:30px;font-weight:500}
.field{position:absolute;top:52px;font-size:8px}
.field .input{width:244px;height:40px;background:var(--white);border-radius:3px;color:#777;font-size:8px;padding:15px 10px;margin-top:6px}
.field small{display:block;font-size:7.5px;margin-top:4px}
.foot-brand{position:absolute;left:119px;top:285px;display:flex;align-items:center;gap:10px;font-size:20px;font-weight:600}
.foot-brand i{width:22px;height:22px;border-radius:50%;background:var(--white);display:block}
.foot-tag{position:absolute;left:119px;top:379px;width:290px;font-size:12.5px;line-height:16px}
.foot-col h3{position:absolute;top:286px;font-size:17px;font-weight:500;letter-spacing:.5px}
.foot-links{position:absolute;left:427px;top:332px;list-style:none;font-size:11.5px}
.foot-links li{height:38.5px}
.contact-item{position:absolute;left:753px;display:flex;align-items:center;gap:16px;font-size:12.5px;line-height:15px}
.contact-item .ic{width:24px;height:24px;border:1.5px solid var(--white);border-radius:50%;display:flex;align-items:center;justify-content:center}
.bottom-bar{position:absolute;left:0;top:546px;width:1200px;height:30px;background:var(--forest-dark);font-size:11.5px;padding:7px 119px}
.social{position:absolute;top:3px;width:24px;height:24px;border:1.5px solid var(--white);border-radius:50%}
</style>
</head>
<body>

<header class="site-header">
  <div class="brand"><i></i><span>BrightHollow<br>Money</span></div>
  <nav class="main-nav">
    <a class="active">HOME</a><a>ABOUT US</a><a>FINANCIAL WELLNESS INFORMATION</a><a>BLOGS</a><a>NETWORK</a>
  </nav>
  <div class="search">Search here
    <svg width="12" height="12" viewBox="0 0 12 12"><circle cx="5" cy="5" r="3.8" fill="none" stroke="#222" stroke-width="1.4"/><line x1="8" y1="8" x2="11" y2="11" stroke="#222" stroke-width="1.4"/></svg>
  </div>
  <div class="account">MY ACCOUNT</div>
</header>

<section class="hero">
  <div class="photo" role="img" aria-label="Two businessmen in suits reviewing documents in a bright office"></div>
  <h1>A CLEARE PATH<br>TO FINANCIAL<br>WELLNESS</h1>
  <p>Having insight to relevent information is what we bring to you in a cleare and easy to digest way.</p>
  <div class="signup">SIGN UP FOR FREE</div>
  <div class="email">ENTER YOUR EMAIL</div>
  <div class="btn go">GET STARTED</div>
</section>

<section class="about">
  <div class="feature-card">
    <div class="photo" role="img" aria-label="Two colleagues by an office window looking at a laptop"></div>
    <h2>We are dedicated to responsibly providing financial services to enable growth and economic progress.</h2>
    <div class="btn btn-outline-light card-btn">LEARN MORE</div>
  </div>
  <div class="eyebrow">OUR BUSINESSES</div>
  <p class="lead">We offer products and services as one integrated institution while treating our clients as one global relationship.</p>
  <div class="btn btn-outline-light lead-btn">LEARN MORE</div>
  <ul class="arrow-list">
    <li>Banking</li><li>Markets</li><li>Services</li><li>U.S. Personal Banking</li><li>Financial Wellness Information</li>
  </ul>
</section>

<section class="news">
  <div class="eyebrow">THE LATEST NEWS FROM US</div>
  <article class="news-card" style="left:121px">
    <div class="tag">PRESS RELEASE</div>
    <h3>Lorem ipsum dolor sit amet, consectetur adipiscing elit, sed do eiusmod tempor inci-didunt ut labore et dolore magna aliqua.</h3>
    <div class="date">March 20, 2023</div>
  </article>
  <div class="divider" style="left:470px"></div>
  <article class="news-card" style="left:512px;width:317px">
    <div class="tag">PRESS RELEASE</div>
    <h3>Lorem ipsum dolor sit amet, consectetur adipiscing elit, sed do eiusmod tempor inci-didunt ut labore et dolore magna aliqua.</h3>
    <div class="date">March 20, 2023</div>
  </article>
  <div class="divider" style="left:869px"></div>
  <article class="news-card" style="left:909px">
    <div class="tag">PRESS RELEASE</div>
    <h3>Lorem ipsum dolor sit amet, consectetur adipiscing elit, sed do eiusmod tempor inci-didunt ut labore et dolore magna aliqua.</h3>
    <div class="date">March 20, 2023</div>
  </article>
  <div class="pager" style="left:122px;top:508px">
    <span class="dim"><svg width="10" height="16"><polyline points="8,2 2,8 8,14" fill="none" stroke="#7dcfbf" stroke-width="1.6"/></svg></span>
    <span><svg width="10" height="16"><polyline points="2,2 8,8 2,14" fill="none" stroke="#0b5d4b" stroke-width="1.6"/></svg></span>
  </div>
  <div class="btn btn-outline-teal" style="left:228px;top:508px;width:114px;height:35px">LEARN MORE</div>
</section>

<section class="impact">
  <div class="eyebrow">OUR IMPACT</div>
  <p class="lead">We’re a organization with a soul:<br>Our business is helping to solve<br>society’s toughest challenges.</p>
  <ul class="arrow-list">
    <li>Sustainability</li><li>Community Action</li><li>Diversity, Equity and Inclusion</li>
  </ul>
  <div class="photo slide-photo" role="img" aria-label="Wind turbine on green hills at sunset"></div>
  <div class="esg">
    <h3>Northvale’s Latest ESG Report</h3>
    <p>Each year, we report on our ESG activities and performance. Here’s a summary of our 2021 activities.</p>
    <div class="btn btn-outline-light">LEARN MORE</div>
  </div>
  <div class="photo next-photo" role="img" aria-label="Team collaborating at a desk in an office"></div>
  <div class="pager" style="left:122px;top:652px">
    <span class="dim"><svg width="10" height="16"><polyline points="8,2 2,8 8,14" fill="none" stroke="#7dcfbf" stroke-width="1.6"/></svg></span>
    <span><svg width="10" height="16"><polyline points="2,2 8,8 2,14" fill="none" stroke="#0b5d4b" stroke-width="1.6"/></svg></span>
  </div>
</section>

<section class="trending">
  <h2>TRENDING IN 2021: FINANCIAL LITERECY</h2>
  <p style="top:167px">Lorem ipsum dolor sit amet, consectetur adipisc-ing elit, sed do eiusmod tempor incididunt ut</p>
  <p style="top:227px">Lorem ipsum dolor sit amet, consectetur adipisc-ing elit, sed do eiusmod tempor incididunt ut labore et dolore magna aliqua. Quis ipsum sus-pendisse ultrices gravida. Risus commodo viverra maecenas accumsan lacus vel facilisis. roin ve-hicula ut neque vitae facilisis. Sed ac odio venenatis, cursus leo eget, dictum massa. In et nisi molestie, molestie turpis at, iaculis lectus. Fusce in purus a odio volutpat sagittis sit amet</p>
  <div class="btn btn-outline-dark">LEARN MORE</div>
  <div class="photo" role="img" aria-label="Bearded man checking his phone beside a laptop"></div>
</section>

<section class="tools">
  <div class="tool" style="left:121px"><div class="box"><svg width="80" height="80" viewBox="0 0 80 80" fill="none" stroke="#fff" stroke-width="3"><circle cx="40" cy="40" r="26"/><circle cx="40" cy="40" r="14"/><line x1="40" y1="4" x2="40" y2="20"/><line x1="40" y1="60" x2="40" y2="76"/><line x1="4" y1="40" x2="20" y2="40"/><line x1="60" y1="40" x2="76" y2="40"/></svg></div><div class="label">SET GOAL</div></div>
  <div class="tool" style="left:284px"><div class="box"><svg width="90" height="90" viewBox="0 0 90 90"><g fill="#fff"><ellipse cx="35" cy="22" rx="22" ry="8"/><rect x="13" y="26" width="44" height="10" rx="4"/><rect x="13" y="40" width="44" height="10" rx="4"/><rect x="13" y="54" width="44" height="10" rx="4"/><circle cx="63" cy="60" r="20"/></g><text x="63" y="68" fill="#3a3a3a" font-size="22" font-weight="700" text-anchor="middle" font-family="Poppins,sans-serif">$</text></svg></div><div class="label">MONEY 101</div></div>
  <div class="tool" style="left:448px"><div class="box"><svg width="90" height="90" viewBox="0 0 90 90"><path d="M48 12 A32 32 0 1 1 20 66 L48 44Z" fill="#fff"/><path d="M52 8 A32 32 0 0 1 82 40 L52 40Z" fill="#fff"/><circle cx="24" cy="50" r="14" fill="#3a3a3a" stroke="#fff" stroke-width="3"/><text x="24" y="56" fill="#fff" font-size="16" font-weight="700" text-anchor="middle" font-family="Poppins,sans-serif">$</text></svg></div><div class="label">BUDGETING</div></div>
  <div class="tool" style="left:611px"><div class="box"><svg width="90" height="90" viewBox="0 0 90 90"><circle cx="45" cy="22" r="13" fill="#fff"/><text x="45" y="28" fill="#3a3a3a" font-size="16" font-weight="700" text-anchor="middle" font-family="Poppins,sans-serif">$</text><path d="M14 46 L32 62 L40 80 L34 80 L28 66 L12 52Z M76 46 L58 62 L50 80 L56 80 L62 66 L78 52Z" fill="#fff"/><rect x="41" y="40" width="8" height="24" fill="#fff"/></svg></div><div class="label">CREDIT<br>MINDFULLNESS</div></div>
  <div class="tool" style="left:774px"><div class="box"><svg width="90" height="90" viewBox="0 0 90 90" fill="none" stroke="#fff" stroke-width="3"><rect x="16" y="14" width="44" height="56"/><line x1="24" y1="26" x2="52" y2="26"/><line x1="24" y1="36" x2="52" y2="36"/><circle cx="36" cy="54" r="10"/><rect x="48" y="40" width="28" height="38" fill="#3a3a3a"/><line x1="54" y1="50" x2="70" y2="50"/><line x1="54" y1="60" x2="70" y2="60"/><line x1="54" y1="70" x2="70" y2="70"/></svg></div><div class="label">DEBT<br>MANAGEMENT</div></div>
  <div class="tool" style="left:939px"><div class="box"><svg width="90" height="90" viewBox="0 0 90 90" fill="none" stroke="#fff" stroke-width="3"><rect x="18" y="14" width="44" height="60" rx="3"/><rect x="30" y="9" width="20" height="9"/><line x1="26" y1="30" x2="36" y2="40"/><line x1="36" y1="30" x2="26" y2="40"/><circle cx="46" cy="50" r="5"/><circle cx="64" cy="64" r="12"/></svg></div><div class="label">RETIREMENT<br>PLANNING</div></div>
</section>

<section class="questions">
  <h2>Have any Questions?</h2>
  <p>Lorem ipsum dolor sit amet, consectetur adipiscing elit, sed do eiusmod tempor incididunt ut labore et dolore magna aliqua. Quis ipsum suspendisse ultrices gravida. Risus commodo viverra maecenas accumsan lacus vel facilisis.</p>
  <div class="btn">CONTACT US</div>
</section>

<footer class="site-footer">
  <div class="newsletter">
    <h2>Sign up to receive the<br>latest news from Us.</h2>
    <div class="field" style="left:327px"><span>Email Address*</span><div class="input">Enter Email</div><small>*Required Field</small></div>
    <div class="field" style="left:584px"><span>Select Preference</span><div class="input">Select</div></div>
  </div>
  <div class="foot-brand"><i></i>BrightHollowMoney</div>
  <p class="foot-tag">Having insight to relevent information is what we bring to you in a cleare and easy to digest way.</p>
  <div class="foot-col"><h3 style="left:427px">IMPORTANT LINKS</h3></div>
  <ul class="foot-links"><li>HOME</li><li>ABOUT US</li><li>FINANCIAL WELLNESS INFORMATION</li><li>BLOGS</li><li>NETWORK</li></ul>
  <div class="foot-col"><h3 style="left:753px">CONTACT US</h3></div>
  <div class="contact-item" style="top:331px"><span class="ic"><svg width="12" height="12" viewBox="0 0 12 12"><path d="M2 1 L4.5 1 L5.5 3.5 L4 4.5 Q5 7 7.5 8 L8.5 6.5 L11 7.5 L11 10 Q6 11 2 6 Q1 3 2 1Z" fill="#fff"/></svg></span>+(555)- 010-2046</div>
  <div class="contact-item" style="top:366px"><span class="ic"><svg width="12" height="10" viewBox="0 0 12 10"><rect x="1" y="1" width="10" height="8" fill="none" stroke="#fff" stroke-width="1.2"/><polyline points="1,1 6,5.5 11,1" fill="none" stroke="#fff" stroke-width="1.2"/></svg></span>hello@brighthollowmoney.net</div>
  <div class="contact-item" style="top:404px"><span class="ic"><svg width="10" height="13" viewBox="0 0 10 13"><path d="M5 12 Q0 6 1 4 A4 4 0 0 1 9 4 Q10 6 5 12Z" fill="#fff"/><circle cx="5" cy="4.5" r="1.5" fill="#7dcfbf"/></svg></span>Lorem ipsum dolor sit amet,<br>consectetur adipiscing elit, sed</div>
  <div class="bottom-bar">Copyeight BrightHollowMoney.net. Allright Reserved.
    <span class="social" style="left:929px"></span><span class="social" style="left:971px"></span><span class="social" style="left:1013px"></span><span class="social" style="left:1053px"></span>
  </div>
</footer>

</body>
</html>
```